Veltrono Goods Inc. - Business Cards, Stationery, etc.
authorized Pembrix distributor
Veltrono Goods Inc. - Business Cards, Stationery, etc. - Industrial Supplies
Creative Brief
Professional
Marcus Delacroix
Chief Financial Officer
412 Quillon Road Sarnia, Ontario N7S 3B9
marc.delacroix@veltronogoods.example
www.veltronogoods.example
Company name is Veltrono Goods Inc. Use company logo "Veltrono" and subtitle, "authorized Pembrix distributor"
Veltrono's mission is to become the supplier of choice for industrial, medical and specialty gases, as well as, welding and safety supplies and equipment, by providing the lowest cost solutions and highest standards of delivery and technical support to our customers.

```html
<!DOCTYPE html>
<html lang="en">
<head>
<meta charset="utf-8">
<title>Veltrono Goods Inc. – Stationery Set</title>
<link rel="stylesheet" href="https://fonts.googleapis.com/css2?family=Open+Sans:wght@400;600;700;800&display=swap">
<style>
  :root{
    --brand-blue:#1f6fb6;
    --accent-red:#c8312c;
    --paper:#ffffff;
    --backdrop:#eef0f2;
    --ink:#4a4f55;
    --ink-soft:#7a8088;
  }
  *{box-sizing:border-box;margin:0;padding:0}
  html,body{width:1200px;height:936px;overflow:hidden}
  body{background:var(--backdrop);font-family:"Open Sans",Arial,sans-serif;color:var(--ink);position:relative}
  .sheet{position:absolute;background:var(--paper);box-shadow:0 3px 10px rgba(0,0,0,.12);overflow:hidden}

  .band{position:absolute;left:0;right:0;background:var(--brand-blue)}
  .red-rule{position:absolute;left:0;right:0;height:2px;background:var(--accent-red)}
  .web{position:absolute;left:0;right:0;text-align:center;color:#fff;font-weight:700;letter-spacing:2px;white-space:nowrap}

  .brand{position:absolute;left:0;right:0;text-align:center;line-height:1}
  .wordmark{display:block;color:var(--brand-blue);font-weight:800;letter-spacing:-.5px}
  .tagline{display:block;color:var(--ink-soft);font-weight:600;white-space:nowrap;margin-top:.35em}

  /* letterhead */
  .letterhead{left:183px;top:66px;width:386px;height:544px}
  .letterhead .band.top{top:0;height:22px}
  .letterhead .brand{top:98px}
  .letterhead .wordmark{font-size:34px}
  .letterhead .tagline{font-size:8px}
  .letterhead .contact{position:absolute;left:20px;right:20px;top:470px;display:flex;flex-wrap:wrap;column-gap:16px;row-gap:4px;font-size:6px;line-height:1.2;color:var(--ink)}
  .letterhead .contact span{white-space:nowrap}
  .letterhead .contact span::before{content:"";display:inline-block;width:5px;height:5px;border-radius:50%;background:var(--brand-blue);margin-right:3px;vertical-align:-1px}
  .letterhead .red-rule{top:500px}
  .letterhead .band.bottom{bottom:0;height:30px}
  .letterhead .web{bottom:9px;font-size:12px}

  /* continuation sheet */
  .sheet-two{left:635px;top:41px;width:462px;height:579px}
  .sheet-two .band.top{top:0;height:26px}
  .sheet-two .brand{top:272px}
  .sheet-two .wordmark{font-size:68px}
  .sheet-two .tagline{font-size:14px}
  .sheet-two .red-rule{top:536px}
  .sheet-two .band.bottom{bottom:0;height:38px}
  .sheet-two .web{bottom:11px;font-size:14px}

  /* business cards */
  .card{left:46px;width:178px;height:102px;border-radius:5px}
  .card-front{top:655px}
  .card-front .band.top{top:0;height:18px}
  .card-front .holder{position:absolute;left:8px;top:3px;color:#fff;font-size:6.5px;font-weight:700;line-height:1.1;white-space:nowrap}
  .card-front .holder small{font-weight:400;font-size:5px;display:block}
  .card-front .brand{top:32px}
  .card-front .wordmark{font-size:20px}
  .card-front .tagline{font-size:5px}
  .card-front .band.bottom{bottom:0;height:24px}
  .card-front .details{position:absolute;left:8px;right:8px;bottom:3px;color:#fff;font-size:4.8px;line-height:1.3}
  .card-front .details span{display:block;white-space:nowrap}
  .card-back{top:782px;background:var(--brand-blue)}
  .card-back .web{top:45px;font-size:8px;letter-spacing:1px}

  /* envelope front */
  .envelope{left:264px;top:671px;width:437px;height:218px}
  .envelope .band.top{top:0;height:14px}
  .envelope .red-rule{top:18px}
  .envelope .brand{top:56px;left:26px;right:auto;text-align:left}
  .envelope .wordmark{font-size:34px}
  .envelope .tagline{font-size:8px}
  .envelope .red-rule.low{top:180px}
  .envelope .band.bottom{bottom:0;height:34px}
  .envelope .web{bottom:10px;font-size:12px}

  /* envelope back */
  .envelope-back{left:737px;top:671px;width:431px;height:218px}
  .envelope-back svg{position:absolute;inset:0}
  .envelope-back .web{top:30px;color:var(--brand-blue);font-size:12px}
</style>
</head>
<body>

<section class="sheet letterhead" aria-label="Letterhead">
  <div class="band top"></div>
  <div class="brand"><span class="wordmark">Veltrono</span><span class="tagline">authorized Pembrix distributor</span></div>
  <div class="contact">
    <span>412 Quillon Road Sarnia, Ontario N7S 3B9</span>
    <span>T 519-555-0142</span>
    <span>F 519-555-0143</span>
    <span>C 519-555-0188</span>
    <span>marc.delacroix@veltronogoods.example</span>
  </div>
  <div class="red-rule"></div>
  <div class="band bottom"></div>
  <div class="web">www.veltronogoods.example</div>
</section>

<section class="sheet sheet-two" aria-label="Continuation sheet">
  <div class="band top"></div>
  <div class="brand"><span class="wordmark">Veltrono</span><span class="tagline">authorized Pembrix distributor</span></div>
  <div class="red-rule"></div>
  <div class="band bottom"></div>
  <div class="web">www.veltronogoods.example</div>
</section>

<section class="sheet card card-front" aria-label="Business card front">
  <div class="band top"></div>
  <div class="holder">Marcus Delacroix<small>Chief Financial Officer</small></div>
  <div class="brand"><span class="wordmark">Veltrono</span><span class="tagline">authorized Pembrix distributor</span></div>
  <div class="band bottom"></div>
  <div class="details">
    <span>412 Quillon Road Sarnia, Ontario N7S 3B9</span>
    <span>C 519-555-0188</span>
    <span>marc.delacroix@veltronogoods.example</span>
  </div>
</section>

<section class="sheet card card-back" aria-label="Business card back">
  <div class="web">www.veltronogoods.example</div>
</section>

<section class="sheet envelope" aria-label="Envelope front">
  <div class="band top"></div>
  <div class="red-rule"></div>
  <div class="brand"><span class="wordmark">Veltrono</span><span class="tagline">authorized Pembrix distributor</span></div>
  <div class="red-rule low"></div>
  <div class="band bottom"></div>
  <div class="web">www.veltronogoods.example</div>
</section>

<section class="sheet envelope-back" aria-label="Envelope back">
  <svg width="431" height="218" viewBox="0 0 431 218">
    <path d="M0 0 H431 V70 L230 120 Q215 124 200 120 L0 70 Z" fill="#f6f7f8" stroke="#e2e5e8"/>
    <path d="M0 150 Q215 120 431 150 V218 H0 Z" fill="#1f6fb6"/>
  </svg>
  <div class="web">www.veltronogoods.example</div>
</section>

</body>
</html>
```